Income Tax Business Cards - Updates

Need to update these business cards while keeping all the same wording but just update them and make them look nicer and more modern/ on brand with our brand.

Industry/Entity Type

finance

Contact Information for Business Card

we have multiple locations so will just need to easily be able to change the address and phone numbers

Colors

Designer to choose colors to be used in the design.

```html
<!DOCTYPE html>
<html lang="en">
<head>
<meta charset="utf-8">
<title>Ledgerline Financial Group – Tax Business Cards</title>
<link rel="stylesheet" href="https://fonts.googleapis.com/css2?family=Montserrat:wght@700;800;900&family=Noto+Serif:wght@700&family=Crimson+Text:wght@400;600&display=swap">
<style>
  :root {
    --brand-green: #0f520b;
    --brand-green-deep: #0a3d07;
    --brand-red: #c40000;
    --paper: #ffffff;
    --ink: #111111;
    --canvas: #ffffff;
  }
  * { box-sizing: border-box; margin: 0; padding: 0; }
  html, body {
    width: 1200px; height: 1200px; overflow: hidden;
    background: var(--canvas);
  }
  .sheet { position: relative; width: 1200px; height: 1200px; }

  .card {
    position: absolute; left: 286px; width: 635px; height: 363px;
    overflow: hidden;
    box-shadow: 0 4px 18px rgba(0,0,0,0.18);
  }
  .card--front { top: 206px; background: var(--paper); }
  .card--back {
    top: 639px; background: var(--brand-green);
    box-shadow: 0 4px 18px rgba(0,0,0,0.18), inset 0 0 40px rgba(0,0,0,0.45);
    border: 1px solid #072e05;
  }

  /* Front */
  .edge-band {
    position: absolute; left: 0; width: 100%; height: 27px;
    background: linear-gradient(var(--brand-green-deep), var(--brand-green) 45%, var(--brand-green-deep));
  }
  .edge-band--top { top: 0; }
  .edge-band--bottom { bottom: 0; }

  .brand-name {
    position: absolute; left: 0; width: 100%; text-align: center;
    font-family: "Crimson Text", serif; font-weight: 600;
    line-height: 1;
  }
  .brand-name__word { display: block; font-size: 54px; letter-spacing: 0.5px; }
  .brand-name__tag { display: block; font-size: 11px; letter-spacing: 4px; margin-top: 8px; }
  .card--front .brand-name { top: 52px; color: var(--brand-green); }
  .card--back .brand-name { top: 40px; color: var(--paper); }

  .cta-band {
    position: absolute; left: 0; top: 159px; width: 100%; height: 45px;
    background: var(--brand-red);
  }
  .cta-band svg { position: absolute; top: 0; }
  .cta-band__text {
    position: absolute; left: 0; width: 100%; top: 0; height: 45px;
    line-height: 46px; text-align: center;
    font-family: "Montserrat", sans-serif; font-weight: 800;
    font-size: 26px; color: var(--paper); letter-spacing: 0.3px;
  }

  .contact { position: absolute; left: 0; width: 100%; text-align: center; color: var(--ink); }
  .contact__phone {
    top: 210px; font-family: "Crimson Text", serif; font-weight: 400;
    font-size: 38px; letter-spacing: 1.5px; line-height: 46px;
  }
  .contact__address {
    top: 262px; font-family: "Noto Serif", serif; font-weight: 700;
    font-size: 18px; line-height: 24px;
  }

  /* Back */
  .offer { position: absolute; left: 0; width: 100%; text-align: center; font-family: "Montserrat", sans-serif; }
  .offer__amount {
    top: 144px; font-weight: 900; font-size: 52px; color: var(--paper);
    line-height: 60px; letter-spacing: -0.5px;
  }
  .offer__headline {
    top: 206px; font-weight: 900; font-size: 28px; color: var(--brand-red);
    line-height: 32px; letter-spacing: -0.5px;
    -webkit-text-stroke: 1px var(--paper); paint-order: stroke fill;
  }
  .offer__note {
    top: 241px; font-weight: 800; font-size: 17px; color: var(--paper);
    line-height: 22px; letter-spacing: -0.2px;
  }
  .brush-stroke {
    position: absolute; left: 138px; top: 280px; width: 358px; height: 68px;
    background: var(--paper);
    transform: rotate(-0.8deg);
  }
  .offer__badge {
    top: 294px; font-weight: 900; font-size: 30px; color: var(--brand-red);
    line-height: 38px; letter-spacing: -0.5px;
  }
</style>
</head>
<body>
<main class="sheet">

  <section class="card card--front" aria-label="Business card front">
    <div class="edge-band edge-band--top"></div>

    <div class="brand-name">
      <span class="brand-name__word">Ledgerline</span>
      <span class="brand-name__tag">FINANCIAL GROUP</span>
    </div>

    <div class="cta-band">
      <svg width="90" height="45" style="left:30px" viewBox="0 0 90 45" aria-hidden="true">
        <g fill="none" stroke="#ffffff" stroke-width="2.5">
          <polyline points="2,0 24,22.5 2,45"/>
          <polyline points="22,0 44,22.5 22,45"/>
          <polyline points="42,0 64,22.5 42,45"/>
          <polyline points="62,0 84,22.5 62,45"/>
        </g>
      </svg>
      <div class="cta-band__text">FILE YOUR TAXES HERE</div>
      <svg width="90" height="45" style="left:518px" viewBox="0 0 90 45" aria-hidden="true">
        <g fill="none" stroke="#ffffff" stroke-width="2.5">
          <polyline points="28,0 6,22.5 28,45"/>
          <polyline points="48,0 26,22.5 48,45"/>
          <polyline points="68,0 46,22.5 68,45"/>
          <polyline points="88,0 66,22.5 88,45"/>
        </g>
      </svg>
    </div>

    <p class="contact contact__phone">(555) 555-5555</p>
    <p class="contact contact__address">Address Line 1<br>Address Line 2<br>Address Line 3</p>

    <div class="edge-band edge-band--bottom"></div>
  </section>

  <section class="card card--back" aria-label="Business card back">
    <div class="brand-name">
      <span class="brand-name__word">Ledgerline</span>
      <span class="brand-name__tag">FINANCIAL GROUP</span>
    </div>

    <p class="offer offer__amount">UP TO $6,000</p>
    <p class="offer offer__headline">SAME DAY ADVANCE</p>
    <p class="offer offer__note">ON APPROVED TAX RETURNS !</p>

    <div class="brush-stroke" role="img" aria-label="White paint brush stroke behind the free estimates message"></div>
    <p class="offer offer__badge">FREE ESTIMATES !</p>
  </section>

</main>
</body>
</html>
```